Facebook Add

I need someone to professional a Facebook add we will supply the information and photos I need people to know the dirt on the roof is actually mould is harming their property

Industry/Entity Type

Exterior house cleaning

Font styles to use
Sans Serif

Colors
0054AA
0677BA
7BADD7
CADEEF
E8F1F8
0094D4
00A9DD
6FCCEA
C7EBF8
E9F6FB
59FF00
82FF00
B8FF75
E3FFCB
F4FFEA
FFF300
FFF600
FEFA6F
FFFEC7
FFFEE8

Requirements
Must have
• Our logo and our image

```html
<!DOCTYPE html>
<html lang="en">
<head>
<meta charset="utf-8">
<title>Harbourside Roof Wash – Roof Mould Ad</title>
<link rel="stylesheet" href="https://fonts.googleapis.com/css2?family=Lilita+One&display=swap">
<style>
  :root {
    --white: #ffffff;
    --sunshine: #f9c80e;
    --ocean: #3a8bb8;
    --navy: #2c4aa4;
    --alert-red: #ef4a4a;
    --ink: #111111;
    --sky: #4fa6ea;
    --roof: #e8542e;
    --leaf: #5b8a2a;
    --page: #ffffff;
  }
  html, body {
    margin: 0;
    padding: 0;
    width: 1200px;
    height: 1070px;
    overflow: hidden;
    background: var(--page);
  }
  .ad {
    position: relative;
    width: 1200px;
    height: 1070px;
    overflow: hidden;
    font-family: "Lilita One", sans-serif;
    background: var(--white);
  }
  .band-yellow {
    position: absolute;
    left: 0; top: 317px;
    width: 1200px; height: 563px;
    background: var(--sunshine);
  }
  .band-blue {
    position: absolute;
    left: 0; top: 880px;
    width: 1200px; height: 190px;
    background: var(--ocean);
  }
  .brand-badge {
    position: absolute;
    left: 103px; top: 78px;
    width: 290px; height: 298px;
    border-radius: 50%;
    background: var(--white);
  }
  .brand {
    position: absolute;
    left: 103px; top: 120px;
    width: 290px;
    text-align: center;
    color: var(--navy);
  }
  .brand-dot {
    display: block;
    width: 64px; height: 64px;
    margin: 0 auto 14px;
    border-radius: 50%;
    background: var(--ocean);
  }
  .brand-name {
    font-size: 38px;
    line-height: 1.05;
  }
  .headline {
    position: absolute;
    left: 61px; top: 452px;
    margin: 0;
    font-size: 50px;
    line-height: 58.5px;
    font-weight: 400;
    color: var(--navy);
  }
  .headline .highlight { color: var(--alert-red); }
  .subline {
    position: absolute;
    left: 61px; top: 712px;
    margin: 0;
    font-size: 34px;
    color: var(--ink);
  }
  .hero-photo {
    position: absolute;
    left: 642px; top: 100px;
    width: 520px; height: 648px;
    border-radius: 130px 0 130px 0;
    background: linear-gradient(180deg, var(--sky) 0%, #7fb8e0 22%, var(--roof) 32%, #c9442a 52%, var(--leaf) 60%, #3f6a22 100%);
  }
  .frames {
    position: absolute;
    left: 0; top: 0;
  }
  .compare-photo {
    position: absolute;
    top: 810px;
    height: 155px;
    border-radius: 26px 0 26px 0;
    background: linear-gradient(180deg, #5aa6e6 0%, #8ec3ea 22%, #d9dcd6 40%, #c8cbc3 78%, #4f6a3a 100%);
  }
  .compare-photo.before { left: 642px; width: 242px; filter: saturate(0.7) brightness(0.92); }
  .compare-photo.after  { left: 937px; width: 223px; }
  .compare-label {
    position: absolute;
    top: 988px;
    width: 200px;
    text-align: center;
    font-size: 34px;
    color: var(--white);
  }
  .compare-label.before { left: 663px; }
  .compare-label.after  { left: 946px; }
  .phone {
    position: absolute;
    left: 58px; top: 906px;
    margin: 0;
    font-size: 72px;
    line-height: 80px;
    color: var(--white);
    letter-spacing: 1px;
  }
  .website {
    position: absolute;
    left: 61px; top: 982px;
    margin: 0;
    font-size: 25px;
    color: var(--white);
  }
  .website .domain { color: var(--sunshine); }
</style>
</head>
<body>
  <main class="ad">
    <div class="band-yellow"></div>
    <div class="band-blue"></div>

    <div class="brand-badge"></div>
    <div class="brand">
      <span class="brand-dot"></span>
      <div class="brand-name">Harbourside<br>Roof Wash</div>
    </div>

    <h1 class="headline">
      Dirt on the<br>
      Roof is actually <span class="highlight">mould</span><br>
      Which is harming<br>
      Your property.
    </h1>
    <p class="subline">Lets us help clean it up !</p>

    <div class="hero-photo" role="img" aria-label="Photo of a freshly cleaned terracotta tile roof behind a leafy green hedge under a blue sky"></div>

    <div class="compare-photo before" role="img" aria-label="Before photo: weatherboard cabin with stained, grimy white walls"></div>
    <div class="compare-photo after" role="img" aria-label="After photo: the same weatherboard cabin with clean bright white walls"></div>

    <svg class="frames" width="1200" height="1070" viewBox="0 0 1200 1070" fill="none" stroke="#ffffff" stroke-width="2">
      <path d="M623 317 V765 H1050 Q1181 765 1181 634 V317"/>
      <path d="M631 975 V835 Q631 801 665 801 H895 V941 Q895 975 861 975 Z"/>
      <path d="M909 975 V835 Q909 801 943 801 H1173 V941 Q1173 975 1139 975 Z"/>
    </svg>

    <span class="compare-label before">Before</span>
    <span class="compare-label after">After</span>

    <p class="phone">1800 555 019</p>
    <p class="website">www.<span class="domain">harboursideroofwash</span>.com.au</p>
  </main>
</body>
</html>
```